RP-Steuerberatung WordPress Site fully implemented (tax advisor)

Hello!
I need a little Wordpress Site for my newly founded Tax-Advisor Company.
I am a one-man Office advising in the area of Crypto-Currency.
PLEASE only provide a Design, if you can also Implement a WP-Site afterwards on an existing Webspace.

Please find the Content and Website-Description in the attached Document

Language for the Website is German (for now)

Target Market(s)

Tax-Advisory (specialized in Crypto Currency)

Coding

Coded - Design and coding required

Number of Pages Required

5+ page

Font styles to use
Sans Serif

Requirements
Must have
• Wordpress Implementation afterwards - Details according to attached Project Information Document

```html
<!DOCTYPE html>
<html lang="de">
<head>
<meta charset="utf-8">
<title>RP-Steuerberatung</title>
<link href="https://fonts.googleapis.com/css2?family=Poppins:wght@400;500;600;700&family=Lato:wght@400;700&display=swap" rel="stylesheet">
<style>
  :root {
    --ink: #ffffff;
    --night: #000000;
    --deep: #05121f;
    --steel: #0e2d45;
    --glow: #1d5a80;
    --button-text: #16243a;
  }
  * { margin: 0; padding: 0; box-sizing: border-box; }
  html, body { width: 1200px; height: 746px; overflow: hidden; background: var(--night); }
  .page { position: relative; width: 1200px; height: 746px; color: var(--ink); font-family: 'Lato', sans-serif; }
  .hero-visual {
    position: absolute; left: 0; top: 0; width: 1200px; height: 669px;
    background:
      radial-gradient(ellipse 420px 300px at 860px 320px, rgba(150,110,90,0.45), transparent 70%),
      radial-gradient(ellipse 600px 420px at 820px 380px, var(--glow), transparent 75%),
      linear-gradient(100deg, var(--night) 0%, var(--deep) 30%, var(--steel) 70%, #0a2236 100%);
  }
  .site-header { position: absolute; left: 0; top: 0; width: 1200px; height: 90px; }
  .brand {
    position: absolute; left: 111px; top: 30px; display: flex; align-items: center; gap: 10px;
    font-family: 'Poppins', sans-serif; font-weight: 600; font-size: 20px; letter-spacing: 0.3px;
  }
  .brand-mark { width: 34px; height: 34px; background: var(--ink); }
  .main-nav { position: absolute; top: 29px; left: 0; font-family: 'Poppins', sans-serif; font-size: 16px; }
  .main-nav a { position: absolute; color: var(--ink); text-decoration: none; white-space: nowrap; }
  .main-nav .is-active { font-weight: 600; border-bottom: 1px solid var(--ink); padding-bottom: 1px; }
  .caret { display: inline-block; margin-left: 8px; border-left: 4px solid transparent; border-right: 4px solid transparent; border-top: 4px solid var(--ink); vertical-align: middle; }
  .hero-title {
    position: absolute; left: 110px; top: 146px; font-family: 'Poppins', sans-serif; font-weight: 600;
    font-size: 50px; line-height: 55px; letter-spacing: 0.5px; text-transform: uppercase;
  }
  .hero-lead { position: absolute; left: 114px; top: 272px; font-size: 15.5px; line-height: 23px; }
  .hero-button {
    position: absolute; left: 111px; top: 326px; width: 151px; height: 53px; border-radius: 6px;
    background: var(--ink); color: var(--button-text); font-family: 'Poppins', sans-serif; font-weight: 500;
    font-size: 18px; display: flex; align-items: center; justify-content: center; text-decoration: none;
  }
  .benefit-list { position: absolute; left: 110px; top: 424px; list-style: none; font-size: 15.5px; }
  .benefit-list li { display: flex; align-items: center; gap: 8px; height: 20px; margin-bottom: 17px; }
  .benefit-list svg { width: 19px; height: 19px; flex: none; }
  .site-footer {
    position: absolute; left: 0; top: 669px; width: 1200px; height: 77px; background: var(--night);
    display: flex; align-items: center; justify-content: center; font-size: 16px;
  }
</style>
</head>
<body>
<div class="page">
  <div class="hero-visual" role="img" aria-label="Hand tippt auf leuchtende Börsenkurven und Kursdiagramme auf dunkelblauem Hintergrund"></div>

  <header class="site-header">
    <div class="brand"><span class="brand-mark"></span><span>RP STEUERBERATUNG</span></div>
    <nav class="main-nav">
      <a class="is-active" href="#" style="left:522px">Heim</a>
      <a href="#" style="left:617px">Leistungen<span class="caret"></span></a>
      <a href="#" style="left:768px">Über mich</a>
      <a href="#" style="left:901px">Kontakt</a>
      <a href="#" style="left:996px">Impressum</a>
    </nav>
  </header>

  <h1 class="hero-title">Willkommen bei<br>RP-Steuerberatung</h1>
  <p class="hero-lead">Ihrem Spezialisten bei allen steuerlichen Themen rund um<br>Einkünfte &amp; Vermögen aus Krypto-Assets.</p>
  <a class="hero-button" href="#">LEISTUNGEN</a>

  <ul class="benefit-list">
    <li><svg viewBox="0 0 20 20"><circle cx="10" cy="10" r="10" fill="#fff"/><path d="M5.5 10.2l3 3 6-6.2" fill="none" stroke="#111" stroke-width="2" stroke-linecap="round" stroke-linejoin="round"/></svg>Dann mach ich eine Schweizer Holding-Gesellschaft– dort zahlt man fast keine Steuern</li>
    <li><svg viewBox="0 0 20 20"><circle cx="10" cy="10" r="10" fill="#fff"/><path d="M5.5 10.2l3 3 6-6.2" fill="none" stroke="#111" stroke-width="2" stroke-linecap="round" stroke-linejoin="round"/></svg>Dann melde ich einfach meinen Hauptwohnsitz in Österreich ab</li>
    <li><svg viewBox="0 0 20 20"><circle cx="10" cy="10" r="10" fill="#fff"/><path d="M5.5 10.2l3 3 6-6.2" fill="none" stroke="#111" stroke-width="2" stroke-linecap="round" stroke-linejoin="round"/></svg>Dann lass ich meine Kryptos auf einer Börse in Singapur, dort ist das steuerfrei</li>
  </ul>

  <footer class="site-footer">Urheberrechte@RP-Steuerberatung.Alle Rechte vorbehalten</footer>
</div>
</body>
</html>
```